Alarm System package Ad for Chatterbox and flyer

Looking to create a Chatterbox add & flyer (A4) for an alarm system package
It will be used in paid Chatterbox advertising and letterbox drops
Once design is decided I will require 2-3 different pricing versions but using the same layout/design

The alarm package is a very cheap deal and the system itself if most suitable for smaller homes and smaller businesses.
The package includes back to base alarm monitoring on a contract for a minimum 12 months. This is at an additional cost (terms and conditions will explain this)

Target Market(s)

families, small business owners, home owners,

Industry/Entity Type

Advertising

Font styles to use
Sans Serif

Colors

Designer to choose colors to be used in the design.

Requirements
Must have
• Harbourline Alarms logo to be easily visible
• the alarm package will be priced at $299 (and 2 other version will be required upon approval of design)
• it will need a section to state terms and conditions apply
• KWL Linked (logo)
• Image of the parts
• minimal wording eg'Fully installed monitored alarm system" then the price
Nice to have
• family and/or home in the background
• Colors similar to my logo
• Logo on the ad
Should not have
• must not have a corporate feel

```html
<!DOCTYPE html>
<html lang="en">
<head>
<meta charset="utf-8">
<title>Harbourline Alarms – Secure Your Home Flyer</title>
<link href="https://fonts.googleapis.com/css2?family=Oswald:wght@500;700&family=Open+Sans:wght@400;600;700&display=swap" rel="stylesheet">
<style>
  :root {
    --navy: #1d3570;
    --sky: #1a9ad6;
    --ink: #1c1c1c;
    --paper: #ffffff;
    --stage: #e9ecef;
    --device: #dfe3e6;
    --photo-a: #6b8a4e;
    --photo-b: #3d4a5c;
  }
  * { box-sizing: border-box; margin: 0; padding: 0; }
  html, body { width: 1200px; height: 966px; overflow: hidden; }
  body { background: var(--stage); font-family: "Open Sans", sans-serif; position: relative; }

  .flyer {
    position: absolute; left: 275px; top: 23px;
    width: 650px; height: 920px;
    background: var(--paper); overflow: hidden;
    box-shadow: 0 6px 24px rgba(0,0,0,.18);
  }
  .flyer-curves { position: absolute; inset: 0; width: 650px; height: 920px; }

  .partner-mark {
    position: absolute; left: 36px; top: 58px;
    display: flex; align-items: center; gap: 12px;
    font-weight: 700; font-size: 32px; color: var(--navy); letter-spacing: -.5px;
  }
  .partner-mark .dot { width: 32px; height: 32px; border-radius: 50%; background: var(--sky); }

  .intro {
    position: absolute; left: 38px; top: 122px; width: 320px;
    font-size: 14px; line-height: 1.3; color: var(--ink);
  }
  .headline {
    position: absolute; left: 36px; top: 192px;
    font-family: "Oswald", sans-serif; font-weight: 500;
    font-size: 38px; line-height: 1; color: var(--sky); text-transform: uppercase; letter-spacing: -.5px;
  }
  .price {
    position: absolute; left: 30px; top: 236px;
    font-family: "Oswald", sans-serif; font-weight: 700; color: var(--navy);
    display: flex; align-items: flex-end; line-height: 1;
  }
  .price .currency { font-size: 42px; margin-right: 4px; margin-bottom: 56px; }
  .price .amount { font-size: 205px; letter-spacing: -4px; }

  .package-parts {
    position: absolute; left: 410px; top: 36px; width: 215px; height: 240px;
    border-radius: 6px;
    background: linear-gradient(160deg, #f4f6f7 0%, var(--device) 70%, #c9ced3 100%);
  }
  .fine-print {
    position: absolute; left: 430px; top: 300px; width: 195px;
    font-size: 9.5px; line-height: 1.4; color: var(--ink);
  }
  .brand {
    position: absolute; left: 452px; top: 378px;
    display: flex; align-items: center; gap: 10px;
    font-weight: 700; font-size: 16px; color: var(--navy); text-transform: uppercase; letter-spacing: 1px; line-height: 1.15;
  }
  .brand .dot { width: 30px; height: 30px; background: var(--navy); border-radius: 50%; flex: none; }
</style>
</head>
<body>
  <article class="flyer">
    <svg class="flyer-curves" viewBox="0 0 650 920">
      <defs>
        <linearGradient id="photoTone" x1="0" y1="0" x2="0" y2="1">
          <stop offset="0" stop-color="#3d4a5c"/>
          <stop offset="1" stop-color="#6b8a4e"/>
        </linearGradient>
        <linearGradient id="navyBand" x1="0" y1="0" x2="1" y2="1">
          <stop offset="0" stop-color="#1d3570"/>
          <stop offset="1" stop-color="#2a6fb3"/>
        </linearGradient>
      </defs>
      <circle cx="330" cy="1060" r="570" fill="url(#navyBand)"/>
      <circle cx="300" cy="1070" r="530" fill="#1a9ad6"/>
      <circle cx="282" cy="1080" r="498" fill="#ffffff"/>
      <circle cx="262" cy="1086" r="478" fill="url(#photoTone)" role="img" aria-label="Photo of a young family playing on the lawn in front of their home"/>
    </svg>

    <div class="partner-mark"><span class="dot"></span>KWL Linked</div>

    <p class="intro">The alarm package is a very cheap deal and the system itself if most suitable for smaller homes and smaller businesses.</p>

    <h1 class="headline">Secure your home</h1>

    <div class="price"><span class="currency">$</span><span class="amount">299</span></div>

    <div class="package-parts" role="img" aria-label="Alarm package parts: control panel, keypad, motion sensors, door contact and remote fob"></div>

    <p class="fine-print">The package includes back to base alarm monitoring on a contract for a minimum 12 months. This is at an additional cost (terms and conditions will explain this)</p>

    <div class="brand"><span class="dot"></span><span>Harbourline<br>Alarms</span></div>
  </article>
</body>
</html>
```